Brellick Consulting Updated Web design

We need to update our website, reconfigure some pages, have the availability for people to register for courses and integrate with our on-line store. It must be something were a novice (like myself) can update classes as they are changed almost daily. We offer training to Police, Fire and 911 Operators so it should be themed as such. See current site at brellickconsulting.example It should have a clear POLICE, FIRE, 911 DISPATCH on home screen to bring visitors to their area and we will need subcategory of pages from there. See uploaded site map for details. I will need guidance on how to get your design up and live, small operation and none of us are tech savvy.

Target Market(s)

Police Officers and Departments, Fire Departments and Dispatch 911

Coding

Number of Pages Required

Requirements
Must have
• See uploaded word document with site map

```html
<!DOCTYPE html>
<html lang="en">
<head>
<meta charset="utf-8">
<title>Brellick Consulting – Agency Services</title>
<link rel="stylesheet" href="https://fonts.googleapis.com/css2?family=Montserrat:wght@600;700;800&family=Open+Sans:wght@400;600;700&display=swap">
<style>
:root{
  --navy:#0c1a3a;
  --navy-deep:#081229;
  --blue:#1f4f9c;
  --yellow:#f5b400;
  --text:#5a5a5a;
  --heading:#1c1c1c;
  --white:#ffffff;
  --line:#e4e4e4;
}
*{margin:0;padding:0;box-sizing:border-box}
html,body{width:1200px;height:2912px;overflow:hidden}
body{position:relative;background:var(--white);font-family:"Open Sans",Arial,sans-serif;color:var(--text);font-size:17px;line-height:1.6}
.abs{position:absolute}

/* header */
.site-header{left:0;top:0;width:1200px;height:120px;background:var(--white);z-index:5}
.brand{left:110px;top:0;width:170px;height:170px;background:var(--navy);display:flex;flex-direction:column;align-items:center;justify-content:center;gap:14px;z-index:6}
.brand-square{width:34px;height:34px;background:var(--yellow)}
.brand-name{font-family:"Montserrat",Arial,sans-serif;font-weight:700;color:var(--white);font-size:19px;line-height:1.2;text-align:center}
.top-bar{left:500px;top:14px;display:flex;align-items:center;gap:26px;font-size:15px;color:var(--text)}
.top-bar .item{display:flex;align-items:center;gap:8px}
.store-btn{background:var(--yellow);color:var(--white);font-weight:700;font-size:14px;padding:7px 18px;border-radius:20px;letter-spacing:.5px}
.main-nav{left:300px;top:60px;display:flex;gap:30px;font-family:"Montserrat",Arial,sans-serif;font-weight:700;font-size:16px;color:var(--navy)}
.main-nav .active{color:var(--yellow)}

/* hero */
.hero{left:0;top:120px;width:1200px;height:380px}
.hero-photo{position:absolute;inset:0;background:linear-gradient(100deg,#1a2233 0%,#2c3445 45%,#1b2333 70%,#0f1626 100%)}
.hero-title{position:absolute;left:112px;top:80px;font-family:"Montserrat",Arial,sans-serif;font-weight:800;color:var(--white);font-size:92px;line-height:1.02;letter-spacing:1px}
.hero-curve{position:absolute;left:0;bottom:-2px}

/* sections */
.photo{background:linear-gradient(135deg,#2b3b6a,#6c2b4a 55%,#1d2a4a)}
.section-title{font-family:"Montserrat",Arial,sans-serif;font-weight:700;color:var(--heading);font-size:40px;line-height:1.15}
.sub-title{font-weight:700;color:var(--heading);font-size:19px}
.body-text{font-size:16px;line-height:1.65;color:var(--text)}
.btn-yellow{background:var(--yellow);color:var(--white);font-family:"Montserrat",Arial,sans-serif;font-weight:700;font-size:15px;padding:12px 30px;border-radius:26px;display:inline-block}
.btn-outline{border:2px solid var(--yellow);color:var(--yellow);font-family:"Montserrat",Arial,sans-serif;font-weight:700;font-size:14px;padding:10px 26px;border-radius:26px;display:inline-block}
.contact-line{display:flex;align-items:center;gap:10px;font-size:16px;color:var(--heading)}

.tick-list{list-style:none}
.tick-list li{display:flex;align-items:flex-start;gap:10px;font-size:16px;line-height:1.75}
.tick-list svg{flex:none;margin-top:7px}

.sample-title{font-weight:700;color:var(--heading);font-size:20px}
.towns{display:grid;grid-template-columns:300px 300px;column-gap:30px}

/* footer */
.site-footer{left:0;top:2500px;width:1200px;height:412px}
.footer-bg{position:absolute;left:0;top:0}
.partner-badges{left:110px;top:2580px;width:280px;height:230px}
.badge{position:absolute;border-radius:50%;background:radial-gradient(circle,#c9ccd4 0%,#8d94a6 60%,#4e5670 100%)}
.footer-col{color:var(--white);font-size:15px;line-height:1.75}
.footer-col h4{font-family:"Montserrat",Arial,sans-serif;font-weight:700;font-size:19px;margin-bottom:14px;letter-spacing:.5px}
.footer-col .row{display:flex;align-items:flex-start;gap:10px}
.footer-col svg{margin-top:6px;flex:none}
.bottom-bar{left:0;top:2830px;width:1200px;height:82px;background:var(--navy-deep);display:flex;align-items:center;justify-content:space-between;padding:0 112px;color:var(--white);font-size:14px}
.socials{display:flex;gap:16px}
.socials span{width:40px;height:40px;border:2px solid var(--white);border-radius:50%;display:block}
</style>
</head>
<body>

<header class="site-header abs">
  <div class="top-bar abs">
    <span class="item">
      <svg width="16" height="16" viewBox="0 0 24 24"><path fill="#f5b400" d="M6.6 10.8a15 15 0 0 0 6.6 6.6l2.2-2.2c.3-.3.7-.4 1-.2 1.1.4 2.3.6 3.6.6.6 0 1 .4 1 1V20c0 .6-.4 1-1 1A17 17 0 0 1 3 4c0-.6.4-1 1-1h3.5c.6 0 1 .4 1 1 0 1.3.2 2.5.6 3.6.1.3 0 .7-.2 1z"/></svg>
      555.014.5210
    </span>
    <span class="item">
      <svg width="18" height="14" viewBox="0 0 24 18"><rect x="1" y="1" width="22" height="16" rx="2" fill="none" stroke="#f5b400" stroke-width="2"/><path d="M1 2l11 8 11-8" fill="none" stroke="#f5b400" stroke-width="2"/></svg>
      info@brellickconsulting.example
    </span>
    <span class="store-btn">ONLINE STORE</span>
  </div>
  <nav class="main-nav abs">
    <span>POLICE</span><span>FIRE</span><span>911 DISPATCH</span><span class="active">AGENCY SERVICES</span><span>UPCOMING COURSE LIST</span><span>ABOUT US</span>
  </nav>
</header>

<div class="brand abs">
  <span class="brand-square"></span>
  <span class="brand-name">BRELLICK<br>CONSULTING</span>
</div>

<section class="hero abs">
  <div class="hero-photo" role="img" aria-label="Dark photo of a police officer speaking into a shoulder radio"></div>
  <h1 class="hero-title">AGENCY<br>SERVICES</h1>
  <svg class="hero-curve" width="1200" height="110" viewBox="0 0 1200 110">
    <path d="M0 60 Q600 130 1200 40 L1200 110 L0 110Z" fill="#1f4f9c"/>
    <path d="M0 72 Q600 138 1200 52 L1200 110 L0 110Z" fill="#f5b400"/>
    <path d="M0 80 Q600 146 1200 62 L1200 110 L0 110Z" fill="#ffffff"/>
  </svg>
</section>

<!-- Training -->
<div class="photo abs" style="left:112px;top:548px;width:310px;height:244px" role="img" aria-label="Police officers in high-visibility vests at a roadside stop at night with emergency lights"></div>
<h2 class="section-title abs" style="left:592px;top:552px">TRAINING</h2>
<p class="body-text abs" style="left:592px;top:612px;width:500px">We Provide the best public safety and police related law training in New England. If we do not offer a course that you are interested in contact us – we can customize any training specifically for your needs.</p>
<p class="body-text abs" style="left:592px;top:728px;width:500px">We also offer our new E-LEARNING platform. Your staff can train anytime 24/7 at their own pace and at their own convenience; easily track their progress and certificates are automatically provided upon successful completion.</p>
<span class="btn-yellow abs" style="left:592px;top:848px">COURSES</span>

<!-- Legal reference -->
<h2 class="section-title abs" style="left:112px;top:968px">LEGAL REFERENCE</h2>
<p class="sub-title abs" style="left:112px;top:1022px">Police Officers Law Manual:</p>
<p class="body-text abs" style="left:112px;top:1054px;width:500px">Our Massachusetts Police Officer's Law manual is the most comprehensive reference on the market. It covers criminal procedure, criminal law, juvenile law and motor vehicle law all in one easy to understand manual.</p>
<span class="btn-outline abs" style="left:112px;top:1188px">CLICK HERE FOR MORE INFORMATION</span>
<p class="sub-title abs" style="left:112px;top:1262px">Legal Updates:</p>
<p class="body-text abs" style="left:112px;top:1294px;width:500px">Keep your officers informed with our easy to understand, quickly distributed legal updates! For literally pennies per day your entire department can receive the most up-to-date legal changes. Provide your officers with the tools to succeed. Contact us for pricing and more details.</p>
<div class="contact-line abs" style="left:112px;top:1456px">
  <svg width="18" height="14" viewBox="0 0 24 18"><rect x="1" y="1" width="22" height="16" rx="2" fill="#f5b400"/><path d="M1 2l11 8 11-8" fill="none" stroke="#fff" stroke-width="2"/></svg>
  info@brellickconsulting.example
</div>
<div class="photo abs" style="left:660px;top:960px;width:422px;height:330px;background:linear-gradient(135deg,#e7e3dc,#b9b1a4 55%,#6f6a63)" role="img" aria-label="Close-up of a hand writing notes on a document with a pen"></div>

<!-- Testing -->
<div class="photo abs" style="left:112px;top:1632px;width:310px;height:336px;background:linear-gradient(135deg,#0f1d3f,#24386a 50%,#0b1630)" role="img" aria-label="Rows of uniformed police officers standing in formation"></div>
<h2 class="section-title abs" style="left:592px;top:1640px;width:520px">TESTING/ASSEMENT CENTERS/ HIRING</h2>
<p class="body-text abs" style="left:592px;top:1744px;width:500px">We provide the absolute best testing services to help your agency select the absolute best candidate for your needs. Our examinations are customized to the needs of each individual agency.</p>
<ul class="tick-list abs" style="left:592px;top:1852px;width:500px">
  <li><svg width="14" height="12" viewBox="0 0 14 12"><path d="M1 6l4 4 8-9" fill="none" stroke="#f5b400" stroke-width="2.4"/></svg>Promotional exams and Assessment Centers</li>
  <li><svg width="14" height="12" viewBox="0 0 14 12"><path d="M1 6l4 4 8-9" fill="none" stroke="#f5b400" stroke-width="2.4"/></svg>Entry Level exams (at no cost to your agency!)</li>
  <li><svg width="14" height="12" viewBox="0 0 14 12"><path d="M1 6l4 4 8-9" fill="none" stroke="#f5b400" stroke-width="2.4"/></svg>Specialty Position Testing: detectives, drug units, School Resource Officers and more</li>
</ul>
<p class="body-text abs" style="left:592px;top:2010px;width:520px;color:var(--heading)">Contact us for more information: Phone <span style="color:var(--yellow)">▪</span> (555) 014-5210 or</p>
<div class="contact-line abs" style="left:592px;top:2038px">email <svg width="16" height="12" viewBox="0 0 24 18"><rect x="1" y="1" width="22" height="16" rx="2" fill="#f5b400"/><path d="M1 2l11 8 11-8" fill="none" stroke="#fff" stroke-width="2"/></svg> info@brellickconsulting.example</div>
<p class="sample-title abs" style="left:592px;top:2080px">Here is a small sample of those who have used our testing services:</p>
<div class="towns tick-list abs" style="left:592px;top:2148px">
  <ul class="tick-list">
    <li><svg width="14" height="12" viewBox="0 0 14 12"><path d="M1 6l4 4 8-9" fill="none" stroke="#f5b400" stroke-width="2.4"/></svg>Framingham, MA</li>
    <li><svg width="14" height="12" viewBox="0 0 14 12"><path d="M1 6l4 4 8-9" fill="none" stroke="#f5b400" stroke-width="2.4"/></svg>Harbor Port Authority</li>
    <li><svg width="14" height="12" viewBox="0 0 14 12"><path d="M1 6l4 4 8-9" fill="none" stroke="#f5b400" stroke-width="2.4"/></svg>Yarmouth, MA</li>
    <li><svg width="14" height="12" viewBox="0 0 14 12"><path d="M1 6l4 4 8-9" fill="none" stroke="#f5b400" stroke-width="2.4"/></svg>West Hartford, CT</li>
    <li><svg width="14" height="12" viewBox="0 0 14 12"><path d="M1 6l4 4 8-9" fill="none" stroke="#f5b400" stroke-width="2.4"/></svg>Westport, MA</li>
    <li><svg width="14" height="12" viewBox="0 0 14 12"><path d="M1 6l4 4 8-9" fill="none" stroke="#f5b400" stroke-width="2.4"/></svg>Westport, CT</li>
    <li><svg width="14" height="12" viewBox="0 0 14 12"><path d="M1 6l4 4 8-9" fill="none" stroke="#f5b400" stroke-width="2.4"/></svg>Duxbury, MA</li>
    <li><svg width="14" height="12" viewBox="0 0 14 12"><path d="M1 6l4 4 8-9" fill="none" stroke="#f5b400" stroke-width="2.4"/></svg>Wayland, MA</li>
    <li><svg width="14" height="12" viewBox="0 0 14 12"><path d="M1 6l4 4 8-9" fill="none" stroke="#f5b400" stroke-width="2.4"/></svg>Tewksbury, MA</li>
    <li><svg width="14" height="12" viewBox="0 0 14 12"><path d="M1 6l4 4 8-9" fill="none" stroke="#f5b400" stroke-width="2.4"/></svg>Harwich, MA</li>
  </ul>
  <ul class="tick-list">
    <li><svg width="14" height="12" viewBox="0 0 14 12"><path d="M1 6l4 4 8-9" fill="none" stroke="#f5b400" stroke-width="2.4"/></svg>Salisbury, MA</li>
    <li><svg width="14" height="12" viewBox="0 0 14 12"><path d="M1 6l4 4 8-9" fill="none" stroke="#f5b400" stroke-width="2.4"/></svg>Weymouth, MA</li>
    <li><svg width="14" height="12" viewBox="0 0 14 12"><path d="M1 6l4 4 8-9" fill="none" stroke="#f5b400" stroke-width="2.4"/></svg>Norwalk, CT</li>
    <li><svg width="14" height="12" viewBox="0 0 14 12"><path d="M1 6l4 4 8-9" fill="none" stroke="#f5b400" stroke-width="2.4"/></svg>Greenwich, CT</li>
    <li><svg width="14" height="12" viewBox="0 0 14 12"><path d="M1 6l4 4 8-9" fill="none" stroke="#f5b400" stroke-width="2.4"/></svg>Dennis, MA</li>
    <li><svg width="14" height="12" viewBox="0 0 14 12"><path d="M1 6l4 4 8-9" fill="none" stroke="#f5b400" stroke-width="2.4"/></svg>Bridgewater, MA</li>
    <li><svg width="14" height="12" viewBox="0 0 14 12"><path d="M1 6l4 4 8-9" fill="none" stroke="#f5b400" stroke-width="2.4"/></svg>Bedford, MA</li>
    <li><svg width="14" height="12" viewBox="0 0 14 12"><path d="M1 6l4 4 8-9" fill="none" stroke="#f5b400" stroke-width="2.4"/></svg>Northfield University</li>
    <li><svg width="14" height="12" viewBox="0 0 14 12"><path d="M1 6l4 4 8-9" fill="none" stroke="#f5b400" stroke-width="2.4"/></svg>Walpole, MA</li>
    <li><svg width="14" height="12" viewBox="0 0 14 12"><path d="M1 6l4 4 8-9" fill="none" stroke="#f5b400" stroke-width="2.4"/></svg>Rockport, MA</li>
    <li style="padding-left:24px">And many, many others</li>
  </ul>
</div>

<!-- Footer -->
<footer class="site-footer abs">
  <svg class="footer-bg" width="1200" height="412" viewBox="0 0 1200 412">
    <path d="M0 40 Q600 -30 1200 40 L1200 412 L0 412Z" fill="#1f4f9c"/>
    <path d="M0 54 Q600 -14 1200 54 L1200 412 L0 412Z" fill="#0c1a3a"/>
  </svg>
</footer>
<div class="partner-badges abs">
  <span class="badge" style="left:0;top:0;width:120px;height:120px"></span>
  <span class="badge" style="left:140px;top:20px;width:120px;height:120px"></span>
  <span class="badge" style="left:60px;top:110px;width:116px;height:116px"></span>
</div>
<div class="footer-col abs" style="left:460px;top:2560px">
  <h4>QUICK LINKS</h4>
  <div>Police</div><div>Fire</div><div>911 Dispatch</div><div>Agency Services</div><div>Upcoming Course List</div><div>About Us</div>
</div>
<div class="footer-col abs" style="left:708px;top:2560px">
  <h4>CONTACT US</h4>
  <div>Brellick Consulting, LLC</div>
  <div class="row"><svg width="12" height="16" viewBox="0 0 12 16"><path d="M6 0a6 6 0 0 0-6 6c0 4.5 6 10 6 10s6-5.5 6-10a6 6 0 0 0-6-6zm0 8.5A2.5 2.5 0 1 1 6 3.5a2.5 2.5 0 0 1 0 5z" fill="#f5b400"/></svg><span>P.O. Box 210<br>Harlow, MA 02471</span></div>
  <div class="row" style="margin-top:14px"><svg width="14" height="14" viewBox="0 0 24 24"><path fill="#f5b400" d="M6.6 10.8a15 15 0 0 0 6.6 6.6l2.2-2.2c.3-.3.7-.4 1-.2 1.1.4 2.3.6 3.6.6.6 0 1 .4 1 1V20c0 .6-.4 1-1 1A17 17 0 0 1 3 4c0-.6.4-1 1-1h3.5c.6 0 1 .4 1 1 0 1.3.2 2.5.6 3.6.1.3 0 .7-.2 1z"/></svg><span>Tel (555) 014-5210</span></div>
  <div class="row" style="margin-top:14px"><svg width="14" height="14" viewBox="0 0 16 16"><rect x="1" y="5" width="14" height="9" fill="#f5b400"/><rect x="4" y="1" width="8" height="5" fill="none" stroke="#f5b400" stroke-width="1.6"/></svg><span>Fax (555) 014-4217</span></div>
</div>
<div class="bottom-bar abs">
  <span>Copyright © 2020, Brellick Consulting. All rights reserved.</span>
  <div class="socials"><span></span><span></span><span></span></div>
</div>

</body>
</html>
```